UK garage/funky house night flier

I need a flier design to upload to my SocialPageHub event page and also some printed fliers to promote the event.

Event is in an urban area underneath railway arches so would like a flier to reflect this with an urban background.
Updates

new photos uploaded to be used as possible backgrounds

Target Market(s)

aged 18-30

Industry/Entity Type

House

Requirements
Must have
• The following text on front of flier:

MIDNIGHT KREST PROMOTIONS PRESENTS A NIGHT CALLED…

‘COPPER TUNNEL RHYTHMZ’

Saturday 7th September 2013

@ Dock27, Marlow Lane, Digbeth, Birmingham B7 3QX

9pm till late

DJ’s playing a selection of Funky house/deep house/future garage and old school 2-step garage

(On back of flier......)

Come and enjoy yourself in a friendly, safe environment with like-minded people who are out to have a good time and rave till the early hours. This venue is part outdoor terrace and part indoor with music being played on the Sonorix-Max Soundsystem – so you know it is a night not to be missed!!

This event is guestlist only. Those not on the guest list will not be allowed entry. To get yourself on the guest list go to the SocialPageHub page www.socialpagehub.example/midnightkrestpromotions and join the event ‘Copper Tunnel Rhythmz’

Dresscode: smart. No trainers/tracksuits
Admission fee on the door is £5
Last entry: midnight
Nice to have
• must be portrait, A5 or A6 size

Urban background, maybe at night, a street with old brickwork, maybe some speakers in the foreground.

dock27 logo bottom right

Back of flier to have the map of Dock27

```html
<!DOCTYPE html>
<html lang="en">
<head>
<meta charset="utf-8">
<title>Copper Tunnel Rhythmz – Flier</title>
<link href="https://fonts.googleapis.com/css2?family=Bebas+Neue&family=Oswald:wght@300;400&family=Open+Sans:wght@400;600&family=Courier+Prime:wght@700&display=swap" rel="stylesheet">
<style>
:root{
  --page:#ffffff;
  --rust-dark:#8a2a0c;
  --rust:#c4420e;
  --orange:#ef6d12;
  --orange-bright:#f7931e;
  --yellow:#f5c21b;
  --cream:#fff3d6;
  --tag:#f04e14;
  --crowd:#8e2f10;
  --speaker:#2b2b2b;
  --band-light:#f2f2f2;
  --band-dark:#c9c9c9;
  --ink:#3a3a3a;
}
*{margin:0;padding:0;box-sizing:border-box}
html,body{width:1200px;height:815px;overflow:hidden;background:var(--page)}
.canvas{position:relative;width:1200px;height:815px}
.panel{position:absolute;top:0;height:815px;overflow:hidden}
.front{left:0;width:574px;
  background:radial-gradient(ellipse at 50% 55%,var(--orange-bright) 0%,var(--orange) 35%,var(--rust) 75%,var(--rust-dark) 100%)}
.back{left:626px;width:574px;
  background:linear-gradient(180deg,var(--rust-dark) 0%,var(--rust) 35%,var(--orange) 70%,var(--rust) 100%)}
.art{position:absolute}
.speaker-art{background:radial-gradient(circle,#6d6d6d 0%,var(--speaker) 55%,#111 70%,transparent 71%)}
.front .speaker-main{left:76px;top:47px;width:157px;height:174px}
.front .speaker-top{left:160px;top:47px;width:80px;height:81px}
.front .speaker-small{left:378px;top:151px;width:117px;height:123px}
.front .splash{left:110px;top:172px;width:309px;height:96px;background:var(--yellow);transform:rotate(-2deg);opacity:.92}
.wings{left:12px;top:300px;width:550px;height:170px;
  background:radial-gradient(ellipse at 50% 50%,transparent 30%,rgba(176,106,216,.55) 31%,rgba(245,194,27,.45) 60%,transparent 72%)}
.crowd{left:0;top:500px;width:574px;height:315px;
  background:linear-gradient(180deg,rgba(142,47,16,0) 0%,var(--crowd) 30%,var(--rust-dark) 100%)}
.presenter{position:absolute;left:120px;top:172px;width:300px;text-align:center;
  font-family:"Bebas Neue",sans-serif;font-size:27px;line-height:32px;color:var(--rust-dark);letter-spacing:.5px}
.presenter span{display:block}
.title{position:absolute;left:0;top:0;width:574px;text-align:center;font-family:"Bebas Neue",sans-serif;
  font-weight:400;color:var(--cream);text-shadow:0 3px 6px rgba(60,10,0,.55)}
.title span{position:absolute;left:0;right:0}
.title .l1{top:274px;font-size:88px;line-height:80px}
.title .l2{top:346px;font-size:88px;line-height:80px}
.title .l3{top:412px;font-size:122px;line-height:110px;color:var(--yellow)}
.djs{position:absolute;left:55px;top:672px;width:470px;font-family:"Open Sans",sans-serif;font-size:13px;line-height:18px;color:var(--cream)}
.event-info{position:absolute;left:55px;top:722px;font-family:"Open Sans",sans-serif;font-size:16px;line-height:23px;color:var(--cream)}
.time-tag{position:absolute;left:356px;top:734px;padding:6px 16px;background:var(--tag);
  font-family:"Courier Prime",monospace;font-size:19px;color:var(--cream);transform:rotate(-12deg);
  box-shadow:0 2px 4px rgba(0,0,0,.35)}
.blurb{position:absolute;left:78px;top:58px;width:418px;font-family:"Oswald",sans-serif;font-weight:300;
  font-size:16px;line-height:23px;color:var(--cream)}
.blurb p+p{margin-top:23px}
.back .crowd{top:430px;height:205px}
.back .speaker-main{left:-30px;top:305px;width:170px;height:170px}
.back .speaker-small{left:310px;top:470px;width:80px;height:80px}
.back .splash{left:-30px;top:450px;width:420px;height:44px;background:var(--yellow);transform:rotate(-6deg);opacity:.92}
.info-card{position:absolute;left:150px;top:370px;width:276px;height:176px;background:var(--tag);
  transform:rotate(-12deg);text-align:center;font-family:"Courier Prime",monospace;color:var(--cream);
  padding-top:24px;box-shadow:0 3px 8px rgba(0,0,0,.4);border:3px solid var(--orange-bright)}
.info-card .dress{font-size:17px;line-height:20px}
.info-card .fee{font-size:23px;line-height:26px;margin-top:12px}
.info-card .last{font-size:16px;margin-top:12px}
.venue-band{position:absolute;left:0;top:638px;width:574px;height:159px;
  background:linear-gradient(90deg,var(--band-dark),var(--band-light) 50%,var(--band-dark))}
.venue-name{position:absolute;left:30px;top:55px;font-family:"Oswald",sans-serif;font-weight:400;font-size:46px;
  letter-spacing:4px;color:var(--ink);display:flex;align-items:center;gap:14px}
.venue-name .mark{width:16px;height:16px;background:var(--ink)}
.map{left:346px;top:14px;width:192px;height:122px;background:#dedede;border:1px solid #b0b0b0}
.back-foot{position:absolute;left:0;top:797px;width:574px;height:18px;background:var(--orange)}
</style>
</head>
<body>
<div class="canvas">

  <section class="panel front">
    <div class="art speaker-art speaker-main" role="img" aria-label="Large loudspeaker illustration"></div>
    <div class="art speaker-art speaker-top" role="img" aria-label="Small loudspeaker illustration"></div>
    <div class="art speaker-art speaker-small" role="img" aria-label="Pair of loudspeakers illustration"></div>
    <div class="art splash" role="img" aria-label="Yellow paint splash behind promoter name"></div>
    <div class="presenter">
      <span>Midnight Krest</span>
      <span>Promotions</span>
      <span>presents a night called…</span>
    </div>
    <div class="art wings" role="img" aria-label="Purple and yellow wings spreading behind the title"></div>
    <div class="art crowd" role="img" aria-label="Silhouetted crowd with raised hands"></div>
    <h1 class="title">
      <span class="l1">COPPER</span>
      <span class="l2">TUNNEL</span>
      <span class="l3">RHYTHMZ</span>
    </h1>
    <p class="djs">DJ’s playing a selection of Funky house/deep house/future garage and old school 2-step garage</p>
    <div class="event-info">
      Saturday 7th September 2013<br>
      @ Dock27, Marlow Lane,<br>
      Digbeth, Birmingham B7 3QX
    </div>
    <div class="time-tag">9pm till late</div>
  </section>

  <section class="panel back">
    <div class="blurb">
      <p>Come and enjoy yourself in a friendly, safe environment with like-minded people who are out to have a good time and rave till the early hours. This venue is part outdoor terrace and part indoor with music being played on the Sonorix-Max Soundsystem – so you know it is a night not to be missed!!</p>
      <p>This event is guestlist only. Those not on the guest list will not be allowed entry. To get yourself on the guest list go to the SocialPageHub page www.socialpagehub.example/midnightkrestpromotions and join the event ‘Copper Tunnel Rhythmz’</p>
    </div>
    <div class="art crowd" role="img" aria-label="Silhouetted crowd with raised hands"></div>
    <div class="art splash" role="img" aria-label="Yellow paint streak"></div>
    <div class="art speaker-art speaker-main" role="img" aria-label="Loudspeaker illustration"></div>
    <div class="art speaker-art speaker-small" role="img" aria-label="Small loudspeaker illustration"></div>
    <div class="info-card">
      <div class="dress">Dresscode: smart.<br>No trainers/tracksuits</div>
      <div class="fee">Admission fee<br>on the door is £5</div>
      <div class="last">Last entry: midnight</div>
    </div>
    <div class="venue-band">
      <div class="venue-name"><span class="mark"></span>DOCK27</div>
      <div class="art map" role="img" aria-label="Street map showing the way to Dock27 in Digbeth"></div>
    </div>
    <div class="back-foot"></div>
  </section>

</div>
</body>
</html>
```